WordPress Website for Pain Relief Clinic

I need a WordPress website designed for my laser pain relief clinic. It needs to be a professional, responsive design with 7 pages: Home, Why Choose Us, Treatable Conditions, Testimonials, FAQ, Franchising, Contact Us. Here is logo: https://files.brivoltcdn.com/media.t-w-e-n.com/sitebuilder/472/CalvexaLogoHighQuality.png

Target Market(s)

people with pain,elderly adults,injuries,soreness

Industry/Entity Type

Clinic

Number of Pages Required

5+ page

Colors
0792cd
85abd2

```html
<!DOCTYPE html>
<html lang="en">
<head>
<meta charset="utf-8">
<title>Calvexa Laser Pain Relief</title>
<link href="https://fonts.googleapis.com/css2?family=Open+Sans:wght@400;600;700&display=swap" rel="stylesheet">
<style>
:root{
  --blue:#0792cd;
  --blue-soft:#85abd2;
  --teal:#3fb6cf;
  --ink:#333a40;
  --muted:#7a838a;
  --light:#eef2f5;
  --dark:#2f3336;
  --darker:#222527;
  --white:#ffffff;
}
*{box-sizing:border-box;margin:0;padding:0}
html,body{width:670px;height:1200px;overflow:hidden;background:var(--white)}
body{font-family:"Open Sans",Arial,sans-serif;color:var(--ink);font-size:7px;line-height:1.45}
.page{position:relative;width:670px;height:1200px}
section,header,footer{position:absolute;left:0;width:670px}
.wrap{position:relative;width:600px;margin:0 auto;height:100%}

/* header */
.site-header{top:0;height:58px;background:var(--white)}
.top-line{position:absolute;right:0;top:5px;font-size:6px;color:var(--muted);display:flex;gap:14px}
.brand{position:absolute;left:0;top:16px;display:flex;align-items:center;gap:6px}
.brand-mark{width:14px;height:14px;border-radius:50%;background:var(--blue)}
.brand-name{font-size:11px;font-weight:600;color:var(--blue)}
.nav{position:absolute;right:0;top:27px;display:flex;gap:2px}
.nav a{font-size:6.5px;color:var(--ink);text-decoration:none;padding:5px 7px}
.nav a.active{background:var(--blue);color:var(--white)}

/* hero */
.hero{top:58px;height:178px;background:linear-gradient(120deg,#3c3e40,#8a8d90 45%,#2f3133);}
.hero-photo{position:absolute;inset:0}
.hero-title{position:absolute;right:110px;top:62px;color:var(--white);font-size:17px;font-weight:400;display:flex;align-items:center;gap:6px}
.hero-title i{width:10px;height:10px;background:var(--teal);display:inline-block}
.hero-sub{position:absolute;right:70px;top:92px;color:#dfe6ea;font-size:6px}
.appointment{position:absolute;left:35px;right:35px;bottom:14px;height:34px;background:rgba(7,146,205,.85);display:flex;flex-direction:column;justify-content:center;padding:0 8px;gap:4px}
.appointment-label{color:var(--white);font-size:6px;background:var(--darker);width:110px;padding:1px 4px;position:absolute;top:-10px;left:0}
.fields{display:flex;gap:4px}
.field{flex:1;height:11px;background:rgba(255,255,255,.25);color:var(--white);font-size:5px;padding:2px 4px}
.send{width:40px;flex:none;background:var(--darker);text-align:center}

/* conditions */
.intro{top:236px;height:178px}
.about-box{position:absolute;left:0;top:20px;width:120px}
.about-box h3{font-size:8px;font-weight:600;margin-bottom:4px}
.about-img{height:52px;background:linear-gradient(135deg,#c9b7a8,#8f7d70)}
.about-box p{font-size:5.5px;color:var(--muted);margin:4px 0}
.btn{display:block;background:var(--blue);color:var(--white);text-align:center;font-size:7px;font-weight:600;padding:5px 0}
.conditions{position:absolute;left:160px;top:20px;width:440px;display:grid;grid-template-columns:1fr 1fr;gap:18px 20px}
.condition{display:flex;gap:8px}
.condition svg{flex:none}
.condition h4{font-size:8px;font-weight:600;margin-bottom:2px}
.condition p{font-size:5.5px;color:var(--muted)}

/* faq / about */
.faq-about{top:414px;height:222px;background:var(--light)}
.faq{position:absolute;left:0;top:18px;width:220px}
.sec-title{font-size:9px;font-weight:400;margin-bottom:8px}
.sec-title b{color:var(--blue);font-weight:400}
.acc-head{background:var(--teal);color:var(--white);font-size:5.5px;text-align:center;padding:3px;margin-bottom:2px}
.acc-body{background:var(--white);font-size:5.5px;color:var(--muted);padding:6px;margin-bottom:4px}
.laser{position:absolute;left:250px;top:18px;width:350px}
.laser-img{position:absolute;left:0;top:20px;width:115px;height:80px;background:linear-gradient(135deg,#b9c4cc,#6f7e8a)}
.laser-text{position:absolute;left:128px;top:20px;width:222px;font-size:5.5px;color:var(--muted)}
.laser-more{color:var(--blue);font-size:5.5px;margin-top:10px}

/* media */
.media{top:636px;height:170px;background:var(--dark)}
.media-head{position:absolute;left:0;top:12px;color:var(--white);font-size:8px;display:flex;gap:10px;align-items:center}
.media-head span{font-size:5.5px;color:#b8bfc4}
.media-line{position:absolute;left:0;right:0;top:26px;height:1px;background:#4a4f53}
.thumbs{position:absolute;left:0;right:0;top:40px;display:flex;gap:12px}
.thumb{position:relative;flex:1;height:92px;border:2px solid var(--white)}
.thumb .play{position:absolute;left:50%;top:50%;width:18px;height:18px;margin:-9px;border-radius:50%;background:rgba(255,255,255,.85)}
.t1{background:linear-gradient(135deg,#7c6e64,#b49e8b)}
.t2{background:linear-gradient(135deg,#c7ced3,#8a96a0)}
.t3{background:linear-gradient(135deg,#6e7fa0,#c9b2a0)}
.t4{background:linear-gradient(135deg,#5a6570,#a9b3bb)}

/* patients */
.patients{top:806px;height:156px}
.words{position:absolute;left:0;top:16px;width:260px}
.quote{display:flex;gap:8px;margin-bottom:12px}
.avatar{width:30px;height:30px;flex:none;background:linear-gradient(135deg,#c8b4a4,#8c7a6c)}
.quote p{font-size:5.5px;color:var(--muted)}
.quote b{display:block;font-size:5.5px;color:var(--ink);font-weight:600;margin-top:2px}
.video{position:absolute;left:320px;top:16px;width:280px}
.video-frame{height:112px;background:linear-gradient(135deg,#586470,#b8a898);position:relative}
.video-bar{position:absolute;left:0;right:0;bottom:0;height:8px;background:rgba(0,0,0,.6)}

/* footer */
.site-footer{top:962px;height:224px;background:var(--darker);color:#c5cbcf}
.cols{position:absolute;left:0;right:0;top:18px;display:grid;grid-template-columns:repeat(4,1fr);gap:18px}
.cols h5{color:var(--white);font-size:8px;font-weight:400;margin-bottom:8px}
.cols p{font-size:5.5px;color:#9aa2a8}
.contact-row{display:flex;gap:5px;align-items:flex-start;margin-top:6px;font-size:5.5px}
.map{height:100px;background:linear-gradient(135deg,#e8e4da,#c9d7c2)}
.testi{display:flex;gap:6px}
.testi .avatar{width:26px;height:26px}
.testi-text{background:var(--white);color:var(--muted);font-size:5.5px;padding:5px;margin-top:6px}
.fvideo{height:80px;background:linear-gradient(135deg,#6b7680,#c2ccd3);position:relative}
.fvideo span{position:absolute;left:0;right:0;bottom:0;background:var(--blue);color:var(--white);font-size:5.5px;text-align:center;padding:2px}
.bottom-bar{top:1186px;height:14px;background:var(--teal);color:var(--white);font-size:5.5px;text-align:center;line-height:14px}
</style>
</head>
<body>
<div class="page">

<header class="site-header">
  <div class="wrap">
    <div class="top-line"><span>Call: 1-800-555-0147</span><span>hello@calvexaclinic.com</span></div>
    <div class="brand"><span class="brand-mark"></span><span class="brand-name">Calvexa Laser Pain Relief</span></div>
    <nav class="nav">
      <a class="active">Home</a><a>Why Choose Us</a><a>Treatable Conditions</a><a>Testimonials</a><a>FAQ</a><a>Franchising</a><a>Contact Us</a>
    </nav>
  </div>
</header>

<section class="hero">
  <div class="hero-photo" role="img" aria-label="Close-up of hands resting on a sore shoulder"></div>
  <div class="hero-title">Laser Therapy Beat the Pain <i></i></div>
  <div class="hero-sub">Reduce Pain  Reduce Inflammation  Restore Mobility  GET YOUR LIFE BACK!</div>
  <div class="appointment">
    <div class="appointment-label">Make an Appointment</div>
    <div class="fields">
      <span class="field">Name</span><span class="field">Phone Number</span><span class="field">Email Address</span><span class="field">Appointment Date</span>
    </div>
    <div class="fields">
      <span class="field">Message</span><span class="field send">SEND</span>
    </div>
  </div>
</section>

<section class="intro">
  <div class="wrap">
    <div class="about-box">
      <h3>About Calvexa Laser Pain Relief</h3>
      <div class="about-img" role="img" aria-label="Therapist treating a patient's knee"></div>
      <p>Gentle laser care that helps your body heal itself, with no drugs and no downtime.</p>
      <span class="btn">MORE</span>
    </div>
    <div class="conditions">
      <div class="condition">
        <svg width="22" height="22" viewBox="0 0 22 22"><circle cx="11" cy="11" r="10" fill="var(--blue)"/><path d="M11 5v12M7 8h8M7 14h8" stroke="#fff" stroke-width="1.5"/></svg>
        <div><h4>Back Pain</h4><p>Relief for lower and upper back strain, sciatica and disc pain that limits your day.</p></div>
      </div>
      <div class="condition">
        <svg width="22" height="22" viewBox="0 0 22 22"><circle cx="11" cy="11" r="10" fill="var(--blue)"/><path d="M9 5v6l3 6M13 5v5" stroke="#fff" stroke-width="1.5" fill="none"/></svg>
        <div><h4>Knee Pain</h4><p>Ease arthritis, sprains and worn joints so you can walk and climb with comfort.</p></div>
      </div>
      <div class="condition">
        <svg width="22" height="22" viewBox="0 0 22 22"><circle cx="11" cy="11" r="10" fill="var(--blue)"/><path d="M6 14c2-6 8-8 10-4" stroke="#fff" stroke-width="1.5" fill="none"/></svg>
        <div><h4>Shoulder Pain</h4><p>Treat frozen shoulder, rotator cuff injury and tension that restricts your reach.</p></div>
      </div>
      <div class="condition">
        <svg width="22" height="22" viewBox="0 0 22 22"><circle cx="11" cy="11" r="10" fill="var(--blue)"/><path d="M9 5v9h6" stroke="#fff" stroke-width="1.5" fill="none"/></svg>
        <div><h4>Ankle Pain</h4><p>Recover faster from sprains, tendon strain and swelling around the ankle joint.</p></div>
      </div>
    </div>
  </div>
</section>

<section class="faq-about">
  <div class="wrap">
    <div class="faq">
      <h2 class="sec-title">FAQ's</h2>
      <div class="acc-head">How long does laser treatment take per visit?</div>
      <div class="acc-body">Most sessions last ten to fifteen minutes. Many patients feel relief after the first few visits, and a full plan usually runs a few weeks.</div>
      <div class="acc-head">Is laser therapy painful?</div>
      <div class="acc-head">Who can benefit from treatment?</div>
      <div class="acc-head">Do I need a referral?</div>
    </div>
    <div class="laser">
      <h2 class="sec-title">About <b>Laser Therapy</b></h2>
      <div class="laser-img" role="img" aria-label="Laser device applied to a patient's arm"></div>
      <div class="laser-text">
        <p>Laser therapy is a safe, non-invasive treatment that sends light energy deep into tissue. It boosts blood flow, calms inflammation and speeds natural repair. There are no needles, no drugs and no recovery time, so you can return to normal life right after each visit.</p>
        <p class="laser-more">Read More »</p>
      </div>
    </div>
  </div>
</section>

<section class="media">
  <div class="wrap">
    <div class="media-head">Media <span>View Full Gallery</span></div>
    <div class="media-line"></div>
    <div class="thumbs">
      <div class="thumb t1" role="img" aria-label="Video still of a hand treatment"><span class="play"></span></div>
      <div class="thumb t2" role="img" aria-label="Clinic treatment room"></div>
      <div class="thumb t3" role="img" aria-label="Video still of a clinic interview"><span class="play"></span></div>
      <div class="thumb t4" role="img" aria-label="Video still of a back treatment"><span class="play"></span></div>
    </div>
  </div>
</section>

<section class="patients">
  <div class="wrap">
    <div class="words">
      <h2 class="sec-title">Words from <b>Patients</b></h2>
      <div class="quote">
        <div class="avatar" role="img" aria-label="Patient portrait"></div>
        <p>After years of knee pain I can finally walk my dog again. The staff were kind and the results came fast.<b>Mark D.</b></p>
      </div>
      <div class="quote">
        <div class="avatar" role="img" aria-label="Patient portrait"></div>
        <p>My shoulder feels like new. I tried everything before this, and nothing worked as well as these sessions.<b>Linda R.</b></p>
      </div>
    </div>
    <div class="video">
      <h2 class="sec-title">Video</h2>
      <div class="video-frame" role="img" aria-label="Video of a therapist treating a patient's shoulder"><div class="video-bar"></div></div>
    </div>
  </div>
</section>

<footer class="site-footer">
  <div class="wrap">
    <div class="cols">
      <div>
        <h5>Contact</h5>
        <p>Visit our clinic or call us to book your first session today.</p>
        <div class="contact-row"><svg width="8" height="9" viewBox="0 0 8 9"><path d="M4 9C1 5 1 4 1 3a3 3 0 0 1 6 0c0 1 0 2-3 6z" fill="var(--teal)"/></svg><span>120 Harbor Lane, Suite 4<br>Springfield</span></div>
        <div class="contact-row"><svg width="8" height="8" viewBox="0 0 8 8"><path d="M1 1h2l1 2-1 1a5 5 0 0 0 2 2l1-1 2 1v2C4 8 0 4 1 1z" fill="var(--teal)"/></svg><span>1-800-555-0147</span></div>
        <div class="contact-row"><svg width="8" height="6" viewBox="0 0 8 6"><rect width="8" height="6" fill="var(--teal)"/><path d="M0 0l4 3 4-3" stroke="#222" fill="none"/></svg><span>hello@calvexaclinic.com</span></div>
      </div>
      <div>
        <h5>Get Direction</h5>
        <div class="map" role="img" aria-label="Map showing the clinic location"></div>
      </div>
      <div>
        <h5>Testimonials</h5>
        <div class="testi"><div class="avatar" role="img" aria-label="Patient portrait"></div><p><b style="color:#fff">Jenny</b><br>Patient</p></div>
        <div class="testi-text">Friendly team and real results. My back pain is gone and I sleep through the night again.</div>
      </div>
      <div>
        <h5>Video</h5>
        <div class="fvideo" role="img" aria-label="Video of a back treatment"><span>Back Pain Treatment</span></div>
      </div>
    </div>
  </div>
</footer>

<div class="bottom-bar" style="position:absolute;left:0;width:670px">© Calvexa Laser Pain Relief. All rights reserved.</div>

</div>
</body>
</html>
```